Einladungskarte
Zielgruppe
Hochzeitsgäste zwischen 30 und 40
Aufgabenstellung
Die Einladung hat folgende Eckdaten:
- Format Din A5 (Doppelseitiger DinA 4 gefalzt) Einladungsbogen (wird leichter Karton)
- Zusätzlicher Einlagebogen für Einladungstext
- Stil klassisch/elegant eher schlicht aber jung
- Grundthema Gerberablume (weiß, beige, rot oder orange)
- Hintergrund (hell)
- Zusätzlich zur Einladung wird Bildrecht der Blume für ein Banner auf der Hochzeitswebseite benötigt
- Editierbare Graphikdatei wird benötigt (da der Text der Einladung noch nicht final ist)

```html
<!DOCTYPE html>
<html lang="de">
<head>
<meta charset="utf-8">
<title>Einladung zur Hochzeit</title>
<link href="https://fonts.googleapis.com/css2?family=Pinyon+Script&display=swap" rel="stylesheet">
<style>
  :root {
    --paper: #ffffff;
    --paper-blush: #fbf3f4;
    --ribbon: #c9303f;
    --ribbon-soft: #ecc4c9;
    --fold: #b9b4b5;
    --ink: #2a2324;
    --accent: #c0354a;
    --petal-pink: #e2607a;
    --petal-blush: #f3c9d1;
    --petal-cream: #f8efe9;
  }
  * { margin: 0; padding: 0; box-sizing: border-box; }
  html, body {
    width: 1200px;
    height: 850px;
    overflow: hidden;
    background: var(--paper);
  }
  .card {
    position: relative;
    width: 1200px;
    height: 850px;
    background: linear-gradient(160deg, var(--paper-blush) 0%, var(--paper) 35%, var(--paper) 70%, var(--paper-blush) 100%);
    overflow: hidden;
    font-family: "Pinyon Script", cursive;
    color: var(--ink);
  }
  .fold-line {
    position: absolute;
    left: 600px;
    top: 0;
    width: 1px;
    height: 850px;
    background: var(--fold);
  }
  .ribbon {
    position: absolute;
    background: var(--ribbon);
  }
  .ribbon--horizontal { left: 0; top: 78px; width: 1200px; height: 2px; }
  .ribbon--vertical { left: 1154px; top: 0; width: 2px; height: 850px; }
  .ribbon--shadow { left: 1180px; top: 0; width: 1px; height: 850px; background: var(--ribbon-soft); }
  .flower-knot {
    position: absolute;
    left: 616px;
    top: 0;
    width: 140px;
    height: 140px;
    border-radius: 50%;
    background: radial-gradient(circle at 50% 50%, var(--petal-pink) 0 45%, rgba(226,96,122,0.75) 62%, rgba(226,96,122,0) 72%);
  }
  .flower-bouquet {
    position: absolute;
    left: 470px;
    top: 478px;
    width: 670px;
    height: 372px;
    background: radial-gradient(ellipse 50% 55% at 52% 45%, var(--petal-cream) 0 40%, var(--petal-blush) 68%, rgba(243,201,209,0) 100%);
  }
  .greeting {
    position: absolute;
    left: 72px;
    top: 282px;
    font-size: 50px;
    line-height: 1;
    font-weight: 400;
  }
  .couple {
    position: absolute;
    right: 106px;
    top: 234px;
    font-size: 40px;
    line-height: 1;
    color: var(--accent);
  }
  .title {
    position: absolute;
    left: 664px;
    top: 286px;
    font-size: 48px;
    line-height: 1;
    font-weight: 400;
  }
</style>
</head>
<body>
  <main class="card">
    <div class="ribbon ribbon--horizontal"></div>
    <div class="ribbon ribbon--vertical"></div>
    <div class="ribbon ribbon--shadow"></div>
    <div class="fold-line"></div>

    <div class="flower-knot" role="img" aria-label="Pinke Gerberablüte am Kreuzungspunkt der roten Bänder"></div>

    <p class="greeting">Wir freuen uns auf euch!</p>

    <p class="couple">Lena und Mattis</p>
    <h1 class="title">Einladung zur Hochzeit</h1>

    <div class="flower-bouquet" role="img" aria-label="Foto: zwei weiße Gerberablüten mit pinken Blattspitzen"></div>
  </main>
</body>
</html>
```